facelift of our car wrap design - for Varno Kestel L2

We would like to give our vehicles a facelift. Attached is our current advertising material.
Must-have: The paintwork of our vehicles is and will remain yellow. I would prefer to use the newer company logo, without the coloured bars, as shown in the attachment.
You can find further inspiration at www.blumaaaak.ch.

Target Market(s)

it should be a classic new design

Requirements
Nice to have
• some advertising keywords

```html
<!DOCTYPE html>
<html lang="de">
<head>
<meta charset="utf-8">
<title>Blumaaaak – Fahrzeugbeschriftung Varno Kestel L2</title>
<link rel="stylesheet" href="https://fonts.googleapis.com/css2?family=Jost:wght@300;400;700&display=swap">
<style>
  :root {
    --paint: #f6cc00;
    --paint-shade: #e2b900;
    --ink: #2a1f0c;
    --glass: #bdbdbd;
    --tyre: #1e1e1e;
    --rim: #c9c9c9;
    --lamp: #b3262b;
    --bg: #ffffff;
  }
  html, body { margin: 0; padding: 0; overflow: hidden; background: var(--bg); }
  .canvas { width: 1187px; height: 1200px; display: block; }
  .wrap-text { font-family: "Jost", sans-serif; fill: var(--ink); }
  .claim { font-weight: 300; font-size: 17px; }
  .wordmark { font-weight: 700; }
  .division { font-weight: 300; letter-spacing: 4px; }
  .service { font-weight: 400; }
  .web { font-weight: 400; }
  .body-paint { fill: var(--paint); }
  .body-line { fill: none; stroke: var(--paint-shade); stroke-width: 2; }
  .window { fill: var(--glass); }
  .tyre { fill: var(--tyre); }
  .rim { fill: var(--rim); }
  .lamp { fill: var(--lamp); }
  .icon { fill: var(--ink); }
  .badge { fill: none; stroke: #8a8a8a; stroke-width: 2; }
</style>
</head>
<body>
<svg class="canvas" viewBox="0 0 1187 1200" xmlns="http://www.w3.org/2000/svg">

  <!-- Side view -->
  <g class="van-side">
    <path class="body-paint" d="M72 392 L78 290 Q90 255 150 225 Q230 190 290 168 L390 90 Q420 72 470 70 L1040 67 Q1060 68 1065 80 L1090 300 L1102 360 L1104 380 L1095 410 L1020 414 Q1010 330 950 330 Q890 330 880 418 L320 422 Q312 330 245 330 Q178 330 170 412 L70 400 Z"/>
    <path class="window" d="M305 185 L380 110 Q395 95 420 93 L552 90 Q560 92 560 100 L556 180 Q554 196 540 200 L330 204 Q300 204 305 185 Z"/>
    <path class="body-line" d="M580 72 L580 410 M828 72 L838 408"/>
    <rect class="lamp" x="1066" y="205" width="20" height="88" rx="4"/>
    <circle class="tyre" cx="245" cy="398" r="70"/>
    <circle class="rim" cx="245" cy="398" r="42"/>
    <circle class="tyre" cx="950" cy="398" r="70"/>
    <circle class="rim" cx="950" cy="398" r="42"/>

    <g class="service-icons">
      <circle class="icon" cx="214" cy="232" r="10"/>
      <circle class="icon" cx="240" cy="232" r="10"/>
      <circle class="icon" cx="266" cy="232" r="10"/>
      <circle class="icon" cx="292" cy="232" r="10"/>
    </g>

    <text class="wrap-text claim" x="610" y="110">IHR KOMPETENTER</text>
    <text class="wrap-text claim" x="610" y="129">PARTNER FÜR MODERNE</text>
    <text class="wrap-text claim" x="610" y="148">HAUSTECHNIK</text>

    <g transform="rotate(-17.5 343 336)">
      <text class="wrap-text wordmark" x="343" y="336" font-size="104" textLength="716" lengthAdjust="spacingAndGlyphs">BLUMAAAAK</text>
      <text class="wrap-text division" x="370" y="388" font-size="30" textLength="700" lengthAdjust="spacing">HAUSTECHNIK + BAUSPENGLEREI</text>
    </g>

    <text class="wrap-text web" x="878" y="290" font-size="18">BLUMAAAAK.CH</text>

    <g class="services" text-anchor="end">
      <text class="wrap-text service" x="834" y="326" font-size="15">SANITÄR</text>
      <text class="wrap-text service" x="834" y="345" font-size="15">HEIZUNG | KÄLTE</text>
      <text class="wrap-text service" x="834" y="363" font-size="15">LÜFTUNG | KLIMA</text>
      <text class="wrap-text service" x="834" y="382" font-size="15">KUNDENDIENST</text>
    </g>
    <g class="bullets">
      <circle class="icon" cx="847" cy="320" r="2.5"/>
      <circle class="icon" cx="847" cy="339" r="2.5"/>
      <circle class="icon" cx="847" cy="357" r="2.5"/>
      <circle class="icon" cx="847" cy="376" r="2.5"/>
    </g>
  </g>

  <!-- Rear view -->
  <g class="van-rear">
    <rect class="tyre" x="283" y="1030" width="92" height="100" rx="20"/>
    <rect class="tyre" x="788" y="1030" width="92" height="100" rx="20"/>
    <path class="body-paint" d="M345 555 Q350 545 370 543 L590 540 L800 545 Q818 548 822 560 L860 700 L870 850 L882 960 L884 1062 L283 1062 L285 960 L296 850 L306 700 Z"/>
    <path class="body-line" d="M597 542 L597 1005 M300 1005 L884 1005"/>
    <rect class="lamp" x="288" y="760" width="46" height="135" rx="8"/>
    <rect class="lamp" x="834" y="760" width="46" height="135" rx="8"/>
    <rect class="lamp" x="492" y="551" width="88" height="10" rx="5"/>

    <text class="wrap-text claim" x="583" y="600" font-size="15" text-anchor="middle">IHR KOMPETENTER PARTNER FÜR</text>
    <text class="wrap-text claim" x="583" y="618" font-size="15" text-anchor="middle">MODERNE HAUSTECHNIK</text>

    <text class="wrap-text wordmark" x="373" y="689" font-size="60" textLength="421" lengthAdjust="spacingAndGlyphs">BLUMAAAAK</text>
    <text class="wrap-text division" x="375" y="711" font-size="19" textLength="419" lengthAdjust="spacing">HAUSTECHNIK + BAUSPENGLEREI</text>

    <circle class="badge" cx="777" cy="760" r="17"/>
    <rect class="badge" x="747" y="786" width="61" height="13" rx="2"/>

    <g class="services" text-anchor="end">
      <text class="wrap-text service" x="775" y="866" font-size="17">SANITÄR</text>
      <text class="wrap-text service" x="775" y="888" font-size="17">HEIZUNG | KÄLTE</text>
      <text class="wrap-text service" x="775" y="911" font-size="17">LÜFTUNG | KLIMA</text>
      <text class="wrap-text service" x="775" y="933" font-size="17">KUNDENDIENST</text>
    </g>
    <g class="bullets">
      <circle class="icon" cx="791" cy="860" r="3"/>
      <circle class="icon" cx="791" cy="882" r="3"/>
      <circle class="icon" cx="791" cy="905" r="3"/>
      <circle class="icon" cx="791" cy="927" r="3"/>
    </g>

    <g class="service-icons">
      <circle class="icon" cx="661" cy="969" r="15"/>
      <circle class="icon" cx="700" cy="969" r="15"/>
      <circle class="icon" cx="738" cy="969" r="15"/>
      <circle class="icon" cx="776" cy="969" r="15"/>
    </g>

    <text class="wrap-text web" x="385" y="984" font-size="17">BLUMAAAAK.CH</text>
  </g>
</svg>
</body>
</html>
```